New Web Design Project- Maplebrook Elders

Maplebrook Elders is the Capital regions premiere, non-medical, in-home care & companionship service that unites "junior-senior" caregivers with "senior-senior" care recipients so that senior-seniors can remain safe & independent in their own homes.
Our compassionate "junior-senior" caregivers are all retirees that have already enjoyed rewarding careers and/or have raised families of their own and feel the need to pay-it-forward with their care for older seniors.
Services include grocery shopping, medical or dental appointments, errands, meal preparation & cleanup, light housekeeping, bed making, laundry, hobbies, reading, transportation, entertainment, games, mobility assistance/transfers, respite care, light yard work, pet walking.

Target Market(s)

Grown children of senior-seniors between who are between 55-70, predominantly the daughters (female). End users of services (senior-seniors) are typically 80-100 years old and living in own homes

Industry/Entity Type

Medical

Coding

Coded - Design and coding required

Number of Pages Required

5+ page

Font styles to use
Sans Serif

Colors
3277b5
ec1f27

Requirements
Must have
• supporting photos on each page. Contact us page. Promotional video (done) attached that doesn't take viewers off my site (https://vidshare.example/Kq7PzLm2Wx4).
• Also, need my downloadable brochure (attached).
• The following pages:
• Home. Services. About Us. News. Employment. Contact us. Junior-Seniors Assisting Senior-Seniors. Why non-medical in-home care. Who are junior-seniors?Financial effects of senior care. Do you need care? Does someone you love need care?
Should not have
• Any other photos or images other than what I've supplied.

```html
<!DOCTYPE html>
<html lang="en">
<head>
<meta charset="utf-8">
<title>Maplebrook Elders – Home</title>
<link href="https://fonts.googleapis.com/css2?family=Questrial&display=swap" rel="stylesheet">
<style>
:root{
  --navy:#0c3d80;
  --navy-deep:#0b2c5c;
  --red:#c41f2d;
  --red-bright:#d2232f;
  --ink:#333;
  --muted:#777;
  --line:#cfcfcf;
  --grey-band:#e4e4e4;
  --white:#fff;
}
*{box-sizing:border-box;margin:0;padding:0}
html,body{width:1200px;height:3232px;overflow:hidden;background:var(--white)}
body{font-family:"Questrial",sans-serif;color:var(--ink);position:relative}
.abs{position:absolute}
a{color:inherit;text-decoration:none}

/* header */
.site-header{left:0;top:0;width:1200px;height:104px;background:linear-gradient(#ffffff,#ececec);border-bottom:1px solid #ddd;z-index:2}
.brand{left:86px;top:30px;display:flex;align-items:center;gap:12px}
.brand-mark{width:40px;height:40px;background:var(--navy)}
.brand-name{font-size:32px;color:var(--navy);letter-spacing:-.3px}
.contact-bar{left:582px;top:17px;display:flex;align-items:center;gap:24px;font-size:13px;color:#444;white-space:nowrap}
.contact-bar span{display:flex;align-items:center;gap:10px}
.btn-appt{left:964px;top:10px;width:148px;height:34px;border-radius:17px;background:var(--navy);color:#fff;font-size:12.5px;display:flex;align-items:center;justify-content:center}
.main-nav{left:582px;top:66px;display:flex;font-size:14px;color:#333}
.main-nav a{margin-right:38px}
.main-nav a:last-child{margin-right:0}

.hero{left:0;top:104px;width:1200px;height:654px;background:linear-gradient(100deg,#9a5a44 0%,#d9d2c4 18%,#cfc2ad 45%,#b9855a 55%,#4c4f72 75%,#e9e7e3 100%)}

.call-band{left:0;top:758px;width:1200px;height:99px;background:var(--red-bright);color:#fff}
.call-band .tag{left:90px;top:38px;font-size:23px;letter-spacing:.2px}
.call-band .icon{left:686px;top:26px}
.call-band .cta{left:756px;top:33px;font-size:30px}

/* section headings */
.section-title{left:0;width:1200px;text-align:center;font-size:38px;font-weight:400;color:#333}
.title-rule{left:578px;width:44px;height:4px;background:var(--red)}
.section-sub{left:0;width:1200px;text-align:center;font-size:15.5px;color:var(--muted)}

/* about */
.about-card{width:325px}
.photo{background:linear-gradient(135deg,#c9b29a,#8d6f58)}
.about-card .photo{height:201px}
.about-card h3{margin-top:28px;font-size:17px;font-weight:400;line-height:30px;letter-spacing:.6px;text-transform:uppercase;color:#222}
.about-card .rule{width:43px;height:3px;background:var(--red);margin:22px 0 18px}
.about-card p{font-size:13px;line-height:29px;color:#555}
.btn-pill{display:inline-flex;align-items:center;justify-content:center;width:138px;height:44px;border-radius:22px;background:var(--navy);color:#fff;font-size:14px}
.about-card .btn-pill{margin-top:26px}

.quote-box{left:784px;top:1081px;width:330px;height:496px;background:#fff;box-shadow:0 2px 8px rgba(0,0,0,.25)}
.quote-box h3{height:65px;background:var(--navy);color:#fff;font-weight:400;font-size:27px;padding:16px 0 0 26px}
.field{position:absolute;left:30px;width:270px;border-bottom:1px solid var(--line);font-size:11px;color:#777;padding-bottom:8px}
.quote-submit{position:absolute;left:88px;top:407px;width:153px;height:46px;background:var(--navy);color:#fff;font-size:15px;display:flex;align-items:center;justify-content:center}

/* services */
.services-band{left:0;top:1682px;width:1200px;height:304px;background:var(--grey-band)}
.service-card{top:1878px;width:322px;height:233px;background:var(--red-bright);color:#fff;text-align:center;padding-top:26px}
.service-card svg{display:block;margin:0 auto}
.service-card h4{font-weight:400;font-size:16px;letter-spacing:.8px;margin-top:16px}
.service-card p{font-size:11.5px;line-height:20px;margin:10px auto 0;width:250px}
.service-card .more{display:inline-block;margin-top:12px;border:1px solid rgba(255,255,255,.55);border-radius:14px;font-size:10.5px;padding:5px 22px}
.slider-arrow{top:1912px;width:44px;height:44px;border:2px solid #bbb;border-radius:50%;display:flex;align-items:center;justify-content:center}

/* works */
.work{width:237px;height:170px}

/* footer */
.site-footer{left:0;top:2848px;width:1200px;height:336px;background:var(--navy-deep);color:#fff}
.foot-brand{left:88px;top:80px;display:flex;align-items:center;gap:10px}
.foot-brand .sq{width:32px;height:32px;background:var(--red-bright)}
.foot-brand .name{font-size:26px}
.foot-about{left:88px;top:194px;width:230px}
.foot-about h5,.foot-col h5{font-weight:400;font-size:14px}
.foot-about p{font-size:10.5px;line-height:19px;margin-top:12px;color:#d7deea}
.divider{top:50px;width:1px;height:230px;background:rgba(255,255,255,.25)}
.foot-col{top:70px}
.foot-col ul{list-style:none;margin-top:22px}
.foot-col li{font-size:13px;line-height:31px;display:flex;align-items:center;gap:14px}
.foot-col li::before{content:"→";font-size:11px;color:#9fb0cc}
.newsletter{left:881px;top:110px;display:flex}
.newsletter .input{width:190px;height:41px;background:#fff;color:#666;font-size:10px;padding:14px 10px}
.newsletter .go{width:43px;height:41px;background:var(--red-bright);display:flex;align-items:center;justify-content:center}
.newsletter-note{left:881px;top:188px;width:235px;font-size:10.5px;line-height:19px;color:#d7deea}
.copyright{left:0;top:3184px;width:1200px;height:48px;background:var(--red-bright);color:#fff;font-size:11.5px;text-align:center;line-height:48px}
</style>
</head>
<body>

<header class="abs site-header">
  <div class="abs brand"><span class="brand-mark"></span><span class="brand-name">Maplebrook Elders</span></div>
  <div class="abs contact-bar">
    <span><svg width="16" height="16" viewBox="0 0 24 24"><path fill="#0c3d80" d="M6.6 10.8a15 15 0 006.6 6.6l2.2-2.2a1 1 0 011-.25 11.4 11.4 0 003.6.6 1 1 0 011 1V20a1 1 0 01-1 1A17 17 0 013 4a1 1 0 011-1h3.5a1 1 0 011 1c0 1.250.2 2.45.6 3.6a1 1 0 01-.25 1z"/></svg>(555) 014-2290</span>
    <span><svg width="18" height="14" viewBox="0 0 24 18"><rect width="24" height="18" rx="2" fill="#0c3d80"/><path d="M1 2l11 8 11-8" stroke="#fff" stroke-width="2" fill="none"/></svg>info@maplebrookelders.example</span>
  </div>
  <a class="abs btn-appt" href="#">Make Appointment</a>
  <nav class="abs main-nav">
    <a href="#">Home</a><a href="#">Services</a><a href="#">About Us</a><a href="#">News</a><a href="#">Employment</a><a href="#">Contact Us</a>
  </nav>
</header>

<div class="abs hero" role="img" aria-label="Photo of a caregiver handing a basket of groceries to a senior woman at her front door"></div>

<section class="abs call-band">
  <div class="abs tag">THE CARE AND COMPANY YOU NEED TO BE AT HOME</div>
  <svg class="abs icon" width="48" height="48" viewBox="0 0 48 48"><circle cx="24" cy="24" r="22" fill="none" stroke="#fff" stroke-opacity=".7" stroke-width="2"/><path transform="translate(13 13) scale(.92)" fill="#fff" d="M6.6 10.8a15 15 0 006.6 6.6l2.2-2.2a1 1 0 011-.25 11.4 11.4 0 003.6.6 1 1 0 011 1V20a1 1 0 01-1 1A17 17 0 013 4a1 1 0 011-1h3.5a1 1 0 011 1c0 1.25.2 2.45.6 3.6a1 1 0 01-.25 1z"/></svg>
  <div class="abs cta">Call 555-014-2290 today!</div>
</section>

<!-- about -->
<h2 class="abs section-title" style="top:920px">About Us</h2>
<div class="abs title-rule" style="top:978px"></div>
<p class="abs section-sub" style="top:1006px">Our mission is to provide the best service, care and match for you and your family</p>

<article class="abs about-card" style="left:86px;top:1081px">
  <div class="photo" role="img" aria-label="Photo of a caregiver cooking a meal with a senior woman"></div>
  <h3>Junior Seniors assisting<br>Senior Seniors</h3>
  <div class="rule"></div>
  <p>Maplebrook Elders is a non-medical in-home and away care and companionship service that unites younger, retired caregivers, or Junior Seniors, with older seniors, or Senior Seniors.</p>
  <a class="btn-pill" href="#">Learn More</a>
</article>

<article class="abs about-card" style="left:435px;top:1081px">
  <div class="photo" style="background:linear-gradient(135deg,#b8c79a,#8e6d79)" role="img" aria-label="Photo of two senior women laughing together on a sofa"></div>
  <h3>Why non-medical in-home<br>care?</h3>
  <div class="rule"></div>
  <p>Our considerate and compassionate Junior Seniors are professionally trained and provide you with the care you need to stay independent, comfortable, and safe in your home.</p>
  <a class="btn-pill" href="#">Learn More</a>
</article>

<form class="abs quote-box">
  <h3>Get a Free Quote</h3>
  <div class="field" style="top:126px">Name*</div>
  <div class="field" style="top:187px">Email*</div>
  <div class="field" style="top:251px">Phone*</div>
  <div class="field" style="top:344px">Message</div>
  <div class="quote-submit">Submit</div>
</form>

<!-- services -->
<div class="abs services-band"></div>
<h2 class="abs section-title" style="top:1724px">Our Services</h2>
<div class="abs title-rule" style="top:1781px"></div>
<p class="abs section-sub" style="top:1809px">Our mission is to provide the best service, care and match for you and your family</p>

<div class="abs slider-arrow" style="left:21px"><svg width="20" height="14" viewBox="0 0 20 14"><path d="M19 7H2M8 1L2 7l6 6" stroke="#bbb" stroke-width="2" fill="none"/></svg></div>
<div class="abs slider-arrow" style="left:1133px"><svg width="20" height="14" viewBox="0 0 20 14"><path d="M1 7h17M12 1l6 6-6 6" stroke="#bbb" stroke-width="2" fill="none"/></svg></div>

<div class="abs service-card" style="left:88px">
  <svg width="46" height="42" viewBox="0 0 46 42"><path d="M23 22s-10-6-10-12a5 5 0 0110-1 5 5 0 0110 1c0 6-10 12-10 12z" fill="#fff"/><path d="M4 14v14l12 10h8M42 14v14L30 38h-8" stroke="#fff" stroke-width="4" fill="none" stroke-linecap="round"/></svg>
  <h4>COMPANIONSHIP</h4>
  <p>A companion-Junior Senior is like the friend who drops by to see how you are faring</p>
  <span class="more">Learn More</span>
</div>
<div class="abs service-card" style="left:437px">
  <svg width="42" height="42" viewBox="0 0 42 42"><path d="M20 3a15 15 0 0115 15c0 4-2 6-2 9v4h-6v8H12v-9a15 15 0 018-27z" fill="#fff"/><circle cx="21" cy="17" r="5" fill="#d2232f"/></svg>
  <h4>ALZHEIMERS CARE</h4>
  <p>The Memory Care Alliance of the Northern Valley provides ongoing training for our Junior Seniors</p>
  <span class="more">Learn More</span>
</div>
<div class="abs service-card" style="left:788px">
  <svg width="48" height="42" viewBox="0 0 48 42"><rect x="2" y="10" width="28" height="20" fill="#fff"/><path d="M31 16h9l6 7v7H31z" fill="#fff"/><circle cx="11" cy="33" r="4" fill="#fff" stroke="#d2232f" stroke-width="2"/><circle cx="38" cy="33" r="4" fill="#fff" stroke="#d2232f" stroke-width="2"/></svg>
  <h4>GENERAL TRANSPORTATION</h4>
  <p>A companion-Junior Senior is like the friend who drops by to see how you are faring</p>
  <span class="more">Learn More</span>
</div>

<!-- works -->
<h2 class="abs section-title" style="top:2204px">Some of our Works</h2>
<div class="abs title-rule" style="top:2261px"></div>
<p class="abs section-sub" style="top:2289px">Our mission is to provide the best service, care and match for you and your family</p>

<div class="abs work photo" style="left:86px;top:2365px;background:linear-gradient(135deg,#cfe3ec,#3e8a9c)" role="img" aria-label="Photo of a smiling caregiver in a plaid shirt"></div>
<div class="abs work photo" style="left:349px;top:2365px;background:linear-gradient(135deg,#eeeeee,#a99a8b)" role="img" aria-label="Photo of a woman using a laptop on a couch"></div>
<div class="abs work photo" style="left:612px;top:2365px;background:linear-gradient(135deg,#6e4a35,#c9a389)" role="img" aria-label="Photo of a caregiver laughing with a senior woman"></div>
<div class="abs work photo" style="left:875px;top:2365px;background:linear-gradient(135deg,#d8d3cc,#6a4a3f)" role="img" aria-label="Photo of a senior couple looking at a tablet"></div>
<div class="abs work photo" style="left:86px;top:2559px;background:linear-gradient(135deg,#b8c79a,#8e6d79)" role="img" aria-label="Photo of two senior women sharing a laugh"></div>
<div class="abs work photo" style="left:349px;top:2559px;background:linear-gradient(135deg,#e7e3d2,#a7b16a)" role="img" aria-label="Photo of two seniors sitting at a table together"></div>
<div class="abs work photo" style="left:612px;top:2559px;background:linear-gradient(135deg,#2f3c34,#8fb04c)" role="img" aria-label="Photo of a caregiver helping a senior at home"></div>
<div class="abs work photo" style="left:875px;top:2559px;background:linear-gradient(135deg,#e6e1da,#9f7a63)" role="img" aria-label="Photo of a caregiver and senior woman smiling together"></div>

<!-- footer -->
<footer class="abs site-footer">
  <div class="abs foot-brand"><span class="sq"></span><span class="name">Maplebrook Elders</span></div>
  <div class="abs foot-about">
    <h5>About Us</h5>
    <p>Totem rem aperiam, eaque ipsa quae ab illo inventore veritatis et quasi architecto beatae vitae dicta sunt explicabo.</p>
  </div>
  <div class="abs divider" style="left:355px"></div>
  <div class="abs foot-col" style="left:424px">
    <h5>Quick Links</h5>
    <ul><li>Home</li><li>Services</li><li>About Us</li><li>News</li><li>Employment</li><li>Contact us</li></ul>
  </div>
  <div class="abs divider" style="left:582px"></div>
  <div class="abs foot-col" style="left:642px">
    <h5>Services</h5>
    <ul><li>Meal preparation</li><li>Light housekeeping</li><li>Bed Making</li><li>Light yard work</li><li>Pet walking</li><li>Laundry</li></ul>
  </div>
  <div class="abs divider" style="left:840px"></div>
  <div class="abs foot-col" style="left:881px"><h5>Subscribe Newsletter</h5></div>
  <div class="abs newsletter">
    <div class="input">Enter Your Email ID...</div>
    <div class="go"><svg width="18" height="13" viewBox="0 0 24 18"><rect width="24" height="18" rx="2" fill="#fff"/><path d="M1 2l11 8 11-8" stroke="#d2232f" stroke-width="2" fill="none"/></svg></div>
  </div>
  <p class="abs newsletter-note">Totem rem aperiam, eaque ipsa quae ab illo inventore veritatis et quasi architecto</p>
</footer>
<div class="abs copyright">maplebrookelders.example 2017. All rights reserved</div>

</body>
</html>
```